Halvern Aviation Group - "Coming Soon" Main Company Webpage

Design a main webpage that can be posted while a fully functional website is constructed. The design should be created to convey a sense of luxury and exclusivity. The main page should contain only one photo as the background. The photo I believe to show "luxury" and "Exclusivity" is listed as "Global Luxury Photo". I have included two other photos as well to aid in providing a variety of presentations.
The "Member PQTR" logo should appear somewhere on the main page but be less prevalent than the main company logo. "Coming Soon" should also appear to convey that a website is being constructed.
Tabs for the website:
- Aircraft Management
- Aircraft Sales
- Pilot Services
- Charter
- Flight Training

```html
<!DOCTYPE html>
<html lang="en">
<head>
<meta charset="UTF-8">
<title>Halvern Aviation Group — Coming Soon</title>
<link rel="stylesheet" href="https://fonts.googleapis.com/css2?family=Play:wght@400;700&display=swap">
<style>
  :root {
    --brand-blue: #0a64b4;
    --ink: #111418;
    --rule: #8fb4d8;
    --field-line: #9aa3ad;
    --white: #ffffff;
    --sky-light: #eef0f2;
    --sky-mid: #cfd3d7;
    --sky-dark: #a9aeb3;
  }
  * { margin: 0; padding: 0; box-sizing: border-box; }
  html, body { width: 1200px; height: 657px; overflow: hidden; }
  body { font-family: "Play", sans-serif; color: var(--ink); }

  .page { position: relative; width: 1200px; height: 657px; overflow: hidden; }

  .hero-photo {
    position: absolute; inset: 0;
    background:
      radial-gradient(ellipse 55% 60% at 85% 60%, #f7f8f9 0%, rgba(247,248,249,0) 70%),
      radial-gradient(ellipse 60% 40% at 45% 15%, #fbfbfc 0%, rgba(251,251,252,0) 70%),
      linear-gradient(180deg, var(--sky-light) 0%, var(--sky-mid) 60%, var(--sky-dark) 100%);
  }

  .site-header {
    position: absolute; top: 0; left: 0; right: 0; height: 100px;
  }
  .brand {
    position: absolute; left: 99px; top: 34px;
    display: flex; align-items: center; gap: 10px;
    font-weight: 700; font-size: 22px; color: var(--brand-blue);
    letter-spacing: 0.3px; white-space: nowrap;
  }
  .brand-mark { width: 14px; height: 14px; background: var(--brand-blue); }

  .main-nav {
    position: absolute; top: 39px; left: 400px;
    display: flex; gap: 0;
  }
  .main-nav a {
    font-weight: 700; font-size: 16px; color: var(--ink);
    text-decoration: none; white-space: nowrap;
  }
  .main-nav a:nth-child(1) { position: absolute; left: 0; }
  .main-nav a:nth-child(2) { position: absolute; left: 204px; }
  .main-nav a:nth-child(3) { position: absolute; left: 348px; }
  .main-nav a:nth-child(4) { position: absolute; left: 491px; }
  .main-nav a:nth-child(5) { position: absolute; left: 592px; }

  .announcement { position: absolute; left: 101px; top: 236px; width: 460px; }
  .announcement-title {
    font-weight: 400; font-size: 53px; line-height: 1;
    color: var(--brand-blue); letter-spacing: 0.5px; white-space: nowrap;
  }
  .announcement-rule {
    border: 0; border-top: 1px solid var(--rule);
    width: 456px; margin-top: 23px;
  }
  .announcement-text {
    margin-top: 13px; font-weight: 700; font-size: 21px; line-height: 33px;
  }

  .notify-form {
    position: absolute; left: 101px; top: 409px;
    width: 461px; height: 55px; background: var(--white);
  }
  .email-icon { position: absolute; left: 10px; top: 15px; width: 25px; height: 24px; }
  .email-field {
    position: absolute; left: 43px; top: 10px; width: 260px; height: 36px;
    border: 0; border-bottom: 1px solid var(--field-line);
    font-family: "Play", sans-serif; font-size: 14px; color: var(--ink);
    background: transparent; outline: none;
  }
  .email-field::placeholder { color: var(--ink); }
  .notify-button {
    position: absolute; left: 326px; top: 4px; width: 131px; height: 46px;
    background: var(--brand-blue); color: var(--white); border: 0;
    font-family: "Play", sans-serif; font-weight: 700; font-size: 20px;
  }

  .site-footer { position: absolute; left: 99px; top: 578px; }
  .membership { display: flex; align-items: flex-end; gap: 6px; }
  .membership-badge {
    width: 30px; height: 22px; border-radius: 50%; background: var(--brand-blue);
  }
  .membership-label { font-size: 8px; line-height: 1; color: var(--ink); padding-bottom: 2px; }
  .copyright { margin-top: 18px; font-size: 14px; font-weight: 700; letter-spacing: 0.3px; }
</style>
</head>
<body>
<div class="page">
  <div class="hero-photo" role="img" aria-label="Private business jet fuselage, engine and wing on the tarmac under an overcast sky"></div>

  <header class="site-header">
    <div class="brand"><span class="brand-mark"></span>Halvern Aviation Group</div>
    <nav class="main-nav">
      <a href="#">Aircraft Management</a>
      <a href="#">Aircraft Sales</a>
      <a href="#">Pilot Services</a>
      <a href="#">Charter</a>
      <a href="#">Flight Training</a>
    </nav>
  </header>

  <section class="announcement">
    <h1 class="announcement-title">We’re Coming Soon</h1>
    <hr class="announcement-rule">
    <p class="announcement-text">We’re Coming Soon! We’re working hard to give you the best experience</p>
  </section>

  <form class="notify-form">
    <svg class="email-icon" viewBox="0 0 25 24" fill="none" stroke="#0a64b4" stroke-width="1.4">
      <rect x="1" y="9" width="23" height="14" rx="1"/>
      <path d="M1 9 L12.5 17 L24 9"/>
      <rect x="5" y="1" width="15" height="11" fill="#fff"/>
      <path d="M8 4.5h9M8 7h9"/>
    </svg>
    <input class="email-field" type="email" placeholder="Enter Your Email Address">
    <button class="notify-button" type="button">Notify Me</button>
  </form>

  <footer class="site-footer">
    <div class="membership">
      <span class="membership-badge" role="img" aria-label="Member PQTR badge"></span>
      <span class="membership-label">member of PQTR</span>
    </div>
    <p class="copyright">© 2023 Halvern Aviation Group. All Rights Reserved.</p>
  </footer>
</div>
</body>
</html>
```